Harborline Supply Company Business Card Design

The Business Card will be one side only with Harborline Supplies Company Logo
Card should have:
Name
Title
Office phone Number
Cell Number
email address
Website
Street Address
Our Slogan is Strong and Steady
Looking for something that stands out from other business cards

Target Market(s)

Heavy equipment Lease Company

```html
<!DOCTYPE html>
<html lang="en">
<head>
<meta charset="utf-8">
<title>Harborline Supplies Company – Business Card</title>
<link href="https://fonts.googleapis.com/css2?family=Arimo:wght@400;700&family=Open+Sans:wght@400;600&display=swap" rel="stylesheet">
<style>
  :root {
    --red: #e31b3d;
    --navy: #262a78;
    --white: #ffffff;
    --ink: #1d1d1f;
    --backdrop: #e9e6e2;
  }
  * { box-sizing: border-box; margin: 0; padding: 0; }
  html, body { width: 1200px; height: 871px; overflow: hidden; }
  body {
    background: var(--backdrop);
    font-family: "Open Sans", Arial, sans-serif;
    position: relative;
  }
  .card {
    position: absolute;
    top: 281px;
    width: 540px;
    height: 309px;
    overflow: hidden;
    box-shadow: 0 6px 18px rgba(0,0,0,.18);
  }

  /* Reverse side */
  .card--back { left: 40px; background: var(--red); }
  .back__brand {
    position: absolute;
    top: 112px; left: 0; right: 0;
    display: flex; align-items: center; justify-content: center; gap: 12px;
    font-family: "Arimo", Arial, sans-serif;
    font-weight: 700;
    font-size: 25px;
    letter-spacing: .5px;
    color: var(--white);
  }
  .back__mark { width: 22px; height: 22px; background: var(--white); }
  .back__slogan-line {
    position: absolute; left: 250px; top: 250px;
    width: 330px; height: 1px;
    background: rgba(255,255,255,.55);
    transform: rotate(-32deg); transform-origin: left center;
  }
  .back__slogan {
    position: absolute; left: 300px; top: 262px;
    font-family: "Arimo", Arial, sans-serif;
    font-weight: 700; font-size: 13px; letter-spacing: .6px;
    color: var(--white);
    white-space: nowrap;
    transform: rotate(-32deg); transform-origin: left center;
  }

  /* Front side */
  .card--front { left: 620px; background: var(--white); }
  .front__shapes { position: absolute; inset: 0; }
  .front__brand {
    position: absolute; left: 30px; top: 40px;
    font-family: "Arimo", Arial, sans-serif;
    font-weight: 700; font-size: 24px; letter-spacing: .2px;
    color: var(--red);
    white-space: nowrap;
  }
  .front__person { position: absolute; left: 34px; top: 118px; font-family: "Arimo", Arial, sans-serif; }
  .person__name { font-weight: 700; font-size: 18px; color: var(--red); }
  .person__title { font-weight: 400; font-size: 14px; color: var(--navy); margin-top: 2px; padding-left: 4px; }
  .front__address {
    position: absolute; left: 38px; top: 184px;
    font-size: 12.5px; color: var(--ink);
  }
  .contact-list {
    position: absolute; left: 34px; top: 220px;
    list-style: none;
  }
  .contact-list li {
    display: flex; align-items: center; gap: 9px;
    font-size: 12.5px; color: var(--white);
    height: 20px;
  }
  .contact-list svg { width: 12px; height: 12px; flex: none; }
</style>
</head>
<body>

  <section class="card card--back" aria-label="Business card reverse">
    <div class="back__brand"><span class="back__mark"></span>HARBORLINE SUPPLIES COMPANY</div>
    <div class="back__slogan-line"></div>
    <p class="back__slogan">STRONG AND STEADY</p>
  </section>

  <section class="card card--front" aria-label="Business card front">
    <svg class="front__shapes" viewBox="0 0 540 309" preserveAspectRatio="none" aria-hidden="true">
      <polygon points="0,212 330,212 400,309 0,309" fill="var(--red)"/>
      <polygon points="390,250 500,190 540,160 540,309 430,309" fill="var(--red)"/>
      <polygon points="505,180 540,130 540,160" fill="var(--red)"/>
    </svg>

    <div class="front__brand">HARBORLINE SUPPLIES COMPANY</div>

    <div class="front__person">
      <p class="person__name">DANA WHITFIELD</p>
      <p class="person__title">PRESIDENT</p>
    </div>

    <p class="front__address">Street Name, City Name, Zipcode - 01234</p>

    <ul class="contact-list">
      <li>
        <svg viewBox="0 0 12 12"><path d="M2.5 1 L4.5 1 L5.2 3.6 L4 4.6 Q5 7 7.4 8 L8.4 6.8 L11 7.5 L11 9.5 Q11 11 9.5 11 Q1 10.5 1 2.5 Q1 1 2.5 1Z" fill="var(--white)"/></svg>
        012-555-0147
      </li>
      <li>
        <svg viewBox="0 0 12 12"><rect x="3" y="0.8" width="6" height="10.4" rx="1.2" fill="none" stroke="var(--white)" stroke-width="1.2"/><circle cx="6" cy="9.2" r=".7" fill="var(--white)"/></svg>
        012-555-0147
      </li>
      <li>
        <svg viewBox="0 0 12 12"><rect x=".8" y="2.5" width="10.4" height="7" fill="var(--white)"/><path d="M.8 2.5 L6 6.6 L11.2 2.5" fill="none" stroke="var(--red)" stroke-width="1"/></svg>
        office@harborlinesupplies.com
      </li>
      <li>
        <svg viewBox="0 0 12 12"><circle cx="6" cy="6" r="5" fill="none" stroke="var(--white)" stroke-width="1.1"/><ellipse cx="6" cy="6" rx="2.2" ry="5" fill="none" stroke="var(--white)" stroke-width="1"/><path d="M1 6 H11 M2 3.5 H10 M2 8.5 H10" stroke="var(--white)" stroke-width=".9"/></svg>
        www.harborlinesupplies.com
      </li>
    </ul>
  </section>

</body>
</html>
```